Marlow Landscaping Landing Page

I require a landing page for my landscaping business.

My business plan revolves around hooking clients with weeding services. Not lawn herbicide sprays, but actual hand weeding and bed maintenance. I've found my niche as most people do not want to do this kind of work. From there I often upsell clients into actual hardscaping or softscaping.

I like things to be clean, concise, and to the point. Not overly flashy, but not so minimal that that it's boring. My logo is a very good example of what I like.

The business is LGBTQ owned and operated. I do not broadcast this but I feel the logo itself, along with the name is usually enough to tip people into assumption. I'm not opposed to color, but I do not want the page to scream "gay". My favourite color is yellow...

I used to be a door to door salesman so I'm doing something different where I want to do all my selling in my first meeting with the client. With this said I do not need a section for "work pictures", as I have photos of my work on my tablet, which I show the client during the consultation.

Ideally i'd like my web site to actually be just a landing page. I'd like room for all the following information within the page;

- description of services;
Weeding of Perennial and Flower Beds
Selective Pruning of Trees and Shrubs
Hedging
Landscape Construction
Landscape Design
Total Lawn Treatment Plans
Landscape Pest Control

- contact information, phone, email
Gerald Hanswick
204-731-4426
ger.hanswick@brelvanyard.com

- "free estimates" somewhere on the page that is either led to by the eye, or very easy to notice and see

- and my slogan which is "dependable, reliable, consistent"

- room for a link to my future ratewell account so they can see reviews from real people

- My Logo present

Any or all of these can be custom made graphics or simply text, whatever looks best

I do not want people to have to search for information throughout. Design it in such a way that either the eye flows naturally from one piece of information to the other, or that it's all compartmentalized neatly enough that everything is easy to find.

As I am a landscape and outdoor maintenance service I'm no opposed to images such as flowers, trees, landscaping, etc being present. However please note that my main focus and source of income comes from weeding services, everything else is bonus cash.

Many of my clients are extremely wealthy individuals who pay over $1000 for the season for me just to show up and pull weeds. So making the website appeal to wealthy people as opposed to the average joe is paramount.

I do not cut grass. Please do not have any indication on the website, either through writing or graphics that implies that I cut grass. There are enough companies doing that.

Target Market(s)

Wealthy, often elderly individuals.

Industry/Entity Type

Landscape Gardening

Coding

Coded - Design and coding required

Number of Pages Required

1 page

Font styles to use
Sans Serif

Colors

Designer to choose colors to be used in the design.

Requirements
Must have
• - description of services;
• Weeding of Perennial and Flower Beds
• Selective Pruning of Trees and Shrubs
• Hedging
• Landscape Construction
• Landscape Design
• Total Lawn Treatment Plans
• Landscape Pest Control
• - contact information, phone, email
• Gerald Hanswick
• 204-731-4426
• ger.hanswick@brelvanyard.com
• - "free estimates" somewhere on the page that is either led to by the eye, or very easy to notice and see
• - and my slogan which is "dependable, reliable, consistent"
• - room for a link to my future ratewell account so they can see reviews from real people
• - My Logo present
Nice to have
• Flowers or weeds depicted. Possibly some hardscaping and softscaping if it doesnt look too bulky and crowded.
Should not have
• grass

```html
<!DOCTYPE html>
<html lang="en">
<head>
<meta charset="utf-8">
<title>Marlow Landscaping</title>
<link href="https://fonts.googleapis.com/css2?family=Open+Sans:wght@400;600;700&display=swap" rel="stylesheet">
<style>
  :root{
    --orange:#e2531f;
    --ink:#222;
    --text:#555;
    --muted:#888;
    --frame:#eeeeee;
    --card:#f7f7f7;
    --footer:#7b7b7b;
    --footer-panel:#707070;
    --footer-bar:#2f2f2f;
    --link-blue:#cfe6ff;
    --button-blue:#1565d8;
    --white:#fff;
  }
  *{box-sizing:border-box;margin:0;padding:0}
  html,body{width:1114px;height:1200px;overflow:hidden;background:var(--white)}
  body{position:relative;font-family:"Open Sans",Arial,sans-serif;color:var(--text)}
  .abs{position:absolute}
  .page-frame{left:150px;top:11px;width:791px;height:1187px;background:var(--frame);border:1px solid #e2e2e2}
  .content-sheet{left:167px;top:408px;width:774px;height:561px;background:var(--white)}
  .header{left:173px;top:24px;width:764px;height:38px;background:var(--white);border-bottom:3px solid var(--orange)}
  .brand{left:22px;top:6px;display:flex;align-items:center;gap:4px;font-weight:600;font-size:13px;color:var(--ink);letter-spacing:.2px}
  .brand-dot{width:9px;height:9px;border-radius:50%;background:var(--orange)}
  .slogan{left:25px;top:22px;font-size:8.5px;font-weight:700;color:var(--ink);letter-spacing:.3px}
  .main-nav{right:9px;top:22px;display:flex;gap:18px;font-size:6.5px;font-weight:700;color:var(--ink);letter-spacing:.3px}
  .hero{left:173px;top:65px;width:764px;height:299px;background:linear-gradient(180deg,#7fb2e6 0%,#b8d3ea 22%,#c9a98a 40%,#7f8f4a 62%,#8a6a3a 80%,#6f5a34 100%)}
  .hero-tag{left:54px;top:65px;padding:1px 6px;background:var(--orange);color:var(--white);font-weight:700;font-size:17px;letter-spacing:.4px;white-space:nowrap}
  .hero-line{left:58px;padding:0 4px;background:rgba(255,255,255,.55);color:#333;font-size:17px;white-space:nowrap}
  .intro{left:173px;top:364px;width:764px;height:44px;background:var(--white);border:1px solid #e4e4e4;text-align:center;font-size:9.5px;line-height:18px;padding:4px 80px 0}
  .section-title{left:177px;top:421px;font-size:8.5px;font-weight:700;color:var(--ink);letter-spacing:.3px}
  .section-title span{color:var(--orange)}
  .section-rule{left:250px;top:425px;width:678px;height:4px;background:#efefef}
  .service-card{width:174px;height:169px;background:var(--card);text-align:center}
  .service-photo{width:174px;height:121px}
  .service-name{margin-top:18px;font-size:6.5px;font-weight:700;color:var(--ink);letter-spacing:.2px}
  .service-sub{margin-top:4px;font-size:7px;color:var(--orange)}
  .to-top{width:24px;height:24px;background:#e41d1d;display:flex;align-items:center;justify-content:center}
  .feature{width:232px;text-align:center}
  .feature-icon{width:54px;height:54px;border-radius:50%;background:var(--orange);margin:0 auto;display:flex;align-items:center;justify-content:center}
  .feature-title{margin-top:8px;font-size:11.5px;color:#333;letter-spacing:.2px}
  .feature-title b{font-weight:700}
  .feature-text{margin-top:6px;font-size:7.5px;line-height:12px;color:var(--muted)}
  .divider{left:180px;top:942px;width:761px;height:3px;background:#f0f0f0}
  .footer{left:167px;top:969px;width:774px;height:214px;background:var(--footer);color:var(--white)}
  .footer-heading{font-size:11px}
  .footer-links{list-style:none;font-size:9px;line-height:12px}
  .form-panel{left:262px;top:29px;width:309px;height:178px;background:var(--footer-panel)}
  .footer-brand{left:263px;top:14px;font-size:6px;font-weight:600;color:#333;display:flex;align-items:center;gap:2px}
  .footer-brand i{width:5px;height:5px;border-radius:50%;background:var(--orange);display:block}
  .field-label{font-size:7px;color:var(--link-blue)}
  .field{background:var(--white);border:1px solid #ccc;border-radius:2px;font-size:8px;color:#999;padding:3px 5px}
  .send-btn{left:491px;top:189px;width:80px;height:17px;background:var(--button-blue);color:var(--white);font-size:8.5px;text-align:center;line-height:17px;border-radius:2px}
  .office-title{left:594px;top:33px;font-size:13.5px;color:var(--white)}
  .office-rule{left:594px;top:54px;width:173px;height:1px;background:#bbb}
  .office-info{left:594px;font-size:7.5px;color:var(--link-blue);line-height:12px;white-space:nowrap}
  .office-info b{font-weight:700}
  .social{left:624px;top:187px;display:flex;gap:13px}
  .social span{width:14px;height:14px;border-radius:50%;background:var(--white);display:block}
  .footer-bar{left:167px;top:1183px;width:774px;height:15px;background:var(--footer-bar);color:#ddd;font-size:6px;padding:4px 6px}
</style>
</head>
<body>
  <div class="abs page-frame"></div>
  <div class="abs content-sheet"></div>

  <header class="abs header">
    <div class="abs brand">MARLOW LANDSCAPING <span class="brand-dot"></span></div>
    <div class="abs slogan">Dependable, Reliable, Consistent</div>
    <nav class="abs main-nav"><span>HOME</span><span>SERVICES</span><span>ABOUT US</span><span>CONTACT US</span></nav>
  </header>

  <section class="abs hero" role="img" aria-label="Stately home with clipped shrubs, flower beds and a stone walkway">
    <div class="abs hero-tag">FREE ESTIMATES</div>
    <div class="abs hero-line" style="top:104px">Hand Weeding</div>
    <div class="abs hero-line" style="top:127px">Perennial and flower bed care, done by hand</div>
  </section>

  <p class="abs intro">Hand weeding and careful bed maintenance keep perennial and flower beds pristine all season, with no herbicide sprays. Call 204-731-4426 for a free estimate.</p>

  <div class="abs section-title">OUR <span>SERVICES</span></div>
  <div class="abs section-rule"></div>

  <div class="abs service-card" style="left:177px;top:448px"><div class="service-photo" role="img" aria-label="Formal garden with pink and white flower beds" style="background:linear-gradient(160deg,#8aa27c,#d53a86 45%,#f2f0f2 80%,#5d8b3b)"></div><div class="service-name">WEEDING OF PERENNIAL AND FLOWER BEDS</div><div class="service-sub">Done by hand</div></div>
  <div class="abs service-card" style="left:363px;top:448px"><div class="service-photo" role="img" aria-label="Tall clipped hedges under a cloudy sky" style="background:linear-gradient(180deg,#cfdde8,#3f5f2a 40%,#2f4c1f 70%,#5a7a34)"></div><div class="service-name">SELECTIVE PRUNING OF TREES AND SHRUBS</div><div class="service-sub">Healthy growth</div></div>
  <div class="abs service-card" style="left:550px;top:448px"><div class="service-photo" role="img" aria-label="Row of topiary hedges beside a garden path" style="background:linear-gradient(120deg,#4b6b33,#243d18 50%,#a39a86)"></div><div class="service-name">HEDGING</div><div class="service-sub">Crisp lines</div></div>
  <div class="abs service-card" style="left:736px;top:448px"><div class="service-photo" role="img" aria-label="House front with flowering borders" style="background:linear-gradient(180deg,#cfcbb8,#6f8b4a 45%,#b34a8a 65%,#6f7f3f)"></div><div class="service-name">LANDSCAPE CONSTRUCTION</div><div class="service-sub">Built to last</div></div>

  <div class="abs service-card" style="left:177px;top:637px"><div class="service-photo" role="img" aria-label="Curving flower garden with colourful beds" style="background:linear-gradient(150deg,#3d6f2a,#c73b5a 40%,#8a6fc2 60%,#4c7a2a)"></div><div class="service-name">LANDSCAPE DESIGN</div><div class="service-sub">Tailored plans</div></div>
  <div class="abs service-card" style="left:363px;top:637px"><div class="service-photo" role="img" aria-label="Treating red rose bushes" style="background:linear-gradient(135deg,#2f4f1f,#5c7f32 50%,#b72a25 80%,#2f4a1c)"></div><div class="service-name">LANDSCAPE PEST CONTROL</div><div class="service-sub">Plants protected</div></div>
  <div class="abs service-card" style="left:550px;top:637px"><div class="service-photo" role="img" aria-label="Cottage garden flowers behind a white picket fence" style="background:linear-gradient(180deg,#8a9a72,#b94a6a 45%,#e8e4e0 60%,#c34c9a 80%,#5a7a34)"></div><div class="service-name">TOTAL LAWN TREATMENT PLANS</div><div class="service-sub">Season long</div></div>
  <div class="abs service-card" style="left:736px;top:637px"><div class="service-photo" role="img" aria-label="Row of trimmed trees and shrubs along a stone path" style="background:linear-gradient(180deg,#6e9a45,#3a5f24 50%,#8f8a78)"></div><div class="service-name">SELECTIVE PRUNING OF TREES AND SHRUBS</div><div class="service-sub">Expert care</div></div>

  <div class="abs to-top" style="left:917px;top:770px"><svg width="12" height="8" viewBox="0 0 12 8"><path d="M1 7 6 2l5 5" fill="none" stroke="#fff" stroke-width="2.2"/></svg></div>

  <div class="abs feature" style="left:178px;top:805px">
    <div class="feature-icon"><svg width="20" height="20" viewBox="0 0 20 20"><circle cx="10" cy="10" r="6" fill="none" stroke="#fff" stroke-width="3" stroke-dasharray="3 1.7"/><circle cx="10" cy="10" r="2.2" fill="#fff"/></svg></div>
    <div class="feature-title">HAND <b>WEEDING</b></div>
    <p class="feature-text">No sprays, no shortcuts. Every bed is weeded by hand and kept tidy through the season.</p>
  </div>
  <div class="abs feature" style="left:441px;top:805px">
    <div class="feature-icon"><svg width="16" height="20" viewBox="0 0 16 20"><path d="M5 7V5a3 3 0 0 1 6 0v2" fill="none" stroke="#fff" stroke-width="1.6"/><rect x="2" y="7" width="12" height="11" rx="3" fill="#fff"/></svg></div>
    <div class="feature-title">FREE <b>ESTIMATES</b></div>
    <p class="feature-text">Call Gerald Hanswick at 204-731-4426 to book a free on-site consultation and estimate.</p>
  </div>
  <div class="abs feature" style="left:703px;top:805px">
    <div class="feature-icon"><svg width="22" height="22" viewBox="0 0 22 22"><circle cx="11" cy="11" r="10" fill="#fff"/><path d="M11 1v20M1 11h20" stroke="#e2531f" stroke-width="2.4"/></svg></div>
    <div class="feature-title">REAL <b>REVIEWS</b></div>
    <p class="feature-text">Read what our clients say about us on ratewell, with reviews from real people.</p>
  </div>

  <div class="abs divider"></div>

  <footer class="abs footer">
    <div class="abs footer-heading" style="left:65px;top:18px">Navigation</div>
    <ul class="abs footer-links" style="left:75px;top:36px"><li>Homepage</li><li>About Us</li><li>Contac Us</li><li>Your Cart</li><li>Login</li></ul>

    <div class="abs form-panel"></div>
    <div class="abs footer-brand">MARLOW LANDSCAPING <i></i></div>
    <div class="abs field-label" style="left:309px;top:31px">Name</div>
    <div class="abs field" style="left:309px;top:46px;width:218px;height:17px;padding-top:2px">Enter name</div>
    <div class="abs field-label" style="left:309px;top:71px">Email Address</div>
    <div class="abs field" style="left:309px;top:84px;width:218px;height:18px;padding-top:2px">Enter email</div>
    <div class="abs field-label" style="left:309px;top:110px">Message</div>
    <div class="abs field" style="left:309px;top:124px;width:218px;height:53px"></div>
    <div class="abs send-btn">Send Message</div>

    <div class="abs office-title">Our office</div>
    <div class="abs office-rule"></div>
    <div class="abs office-info" style="top:66px"><b>Marlow Landscape</b><br>Gerald Hanswick<br>Fenwick Ridge, CA 94107<br><u>P:</u> 204-731-4426</div>
    <div class="abs office-info" style="top:126px"><b>Email:</b><br><span style="color:#fff">ger.hanswick@brelvanyard.com</span></div>
    <div class="abs office-info" style="top:162px"><b>Read our reviews on ratewell:</b></div>
    <div class="abs social"><span aria-label="Social link"></span><span aria-label="Social link"></span><span aria-label="ratewell reviews"></span><span aria-label="Video channel"></span></div>
  </footer>

  <div class="abs footer-bar">COPYRIGHT 2017 | ALL RIGHT RESERVED.</div>
  <div class="abs to-top" style="left:935px;top:1171px"><svg width="12" height="8" viewBox="0 0 12 8"><path d="M1 7 6 2l5 5" fill="none" stroke="#fff" stroke-width="2.2"/></svg></div>
</body>
</html>
```